Recently launched Investment banking and Corporate Advisory firm focused and experienced on Selling

We are looking for a dynamic Brochure that can highlight our areas of focus, experience and expertise.
We have a small but seasoned team of professionals in the organisation and want to showcase our ability to provide Growth and / or exit solutions for our clients.
We are a boutique firm and want to focus on showcasing the fact that we strive for excellence and quality and not quantity.

Our core business avtivity at this time is Sell Side M&A services (this means that we sell private businesses). We are unique in our approach to "partnering businesses" with other companies...not just selling them. We focus more on the "strategic fit" of the potential partner rather than the simple valuation that a potential partner (buyer) would place on the company.

We have really been focusing on "GROWTH and EXIT" strategies for private business owners. Customers usually talk to us for 1 of two main reasons. Their businesses are usually very stable or rapidly growing , often to a point where the owners are no longer comfortable running them on their own. They often need capital for expansion or a team to help them expand their business into other countries and markets. for this we look for a solution for them and often it is finding them a strategic partner who will want to buy the majority of the business. There are also the clients that are looking for an exit strategy (typically they are older and getting ready to retire) they are typically seeking for a way to exit the business (sell the business).

A tagline I often use is "Customer Vision" - We see our customers business and needs through their eyes.

Our company website is www.keldmoorpartners.com and is a work in progress

Target Market(s)

Business Owners (CEO / Presidents)
Mostly Male
Late 40's to late 60's
Very often they will be Engineers
Very Successful and hard working
Many of them looking for GROWTH solutions
Many of them looking for Retirement
We heavily focus on Oil and Gas Service companies, Oil and Gas manufacturing / oilfield services / Technology Companies and Industrial Companies

Industry/Entity Type

Boutique

Font styles to use
Sans Serif

Colors
f37022
33a6d7

Requirements
Must have
• This must be extremely high quality. The people that will receive these brochures are Presidents and CEO's of companies. Every document we give the customer directly reflects the quality of service we will provide for them.
Nice to have
• Pictures tell a great story and can also tell about the areas of experience and expertise that we have

Ideally we'd be interested in a square shaped marketing document (signifies strength and solidness in the business/opportunity) - either 5x5 or 7x7 size in a 4-6 page (double-sided) saddle-stitched booklet.
We'd like to relay an emotion while also describing our business.

```html
<!DOCTYPE html>
<html lang="en">
<head>
<meta charset="utf-8">
<title>Keldmoor Partners – Mergers &amp; Acquisition Brochure</title>
<link rel="stylesheet" href="https://fonts.googleapis.com/css2?family=Arimo:ital,wght@0,400;0,700;1,400;1,700&family=Playfair+Display:ital,wght@1,700&display=swap">
<style>
  :root {
    --stage: #3b3d40;
    --page-light: #ffffff;
    --page-mid: #e9eaeb;
    --page-dark: #c9cacc;
    --brand-blue: #33a6d7;
    --brand-orange: #f37022;
    --name-blue: #2b6fb3;
    --ink: #1c1c1c;
    --ink-soft: #7a7a7a;
    --rule: #b9babc;
    --white: #ffffff;
  }
  * { box-sizing: border-box; margin: 0; padding: 0; }
  html, body { width: 1200px; height: 643px; overflow: hidden; }
  body { background: var(--stage); font-family: "Arimo", Arial, sans-serif; }

  .spread { position: absolute; left: 45px; top: 45px; width: 1110px; height: 553px; display: flex; }
  .page { position: relative; width: 555px; height: 553px; overflow: hidden; }
  .page--back { background: linear-gradient(90deg, var(--page-light) 0%, var(--page-mid) 70%, var(--page-dark) 100%); }
  .page--cover { background: linear-gradient(90deg, var(--page-dark) 0%, var(--page-mid) 25%, var(--page-light) 100%); border-left: 1px solid #a9aaac; }

  .back-photo {
    position: absolute; left: 153px; top: 17px; width: 250px; height: 260px;
    border: 4px solid var(--white); box-shadow: 0 2px 8px rgba(0,0,0,.45);
    background: linear-gradient(180deg, #c0501a 0%, #e07a25 35%, #b04515 62%, #2a1a12 80%, #120c08 100%);
  }

  .about { position: absolute; left: 152px; top: 313px; width: 262px; }
  .about__title { font-size: 12.5px; font-weight: 700; font-style: italic; color: var(--ink); }
  .about__subtitle { font-size: 12px; font-style: italic; color: var(--ink); margin-top: 8px; }
  .about__text { font-size: 7px; line-height: 9.4px; color: var(--ink-soft); margin-top: 6px; }

  .brand { position: absolute; display: flex; align-items: center; color: var(--name-blue); font-family: "Arimo", Arial, sans-serif; font-weight: 400; }
  .brand__dot { border-radius: 50%; background: var(--brand-blue); flex: none; }
  .brand--back { left: 175px; top: 448px; font-size: 26px; gap: 12px; }
  .brand--back .brand__dot { width: 34px; height: 34px; }
  .brand--cover { left: 22px; top: 476px; font-size: 33px; gap: 16px; }
  .brand--cover .brand__dot { width: 44px; height: 44px; }

  .contact-rule { position: absolute; left: 30px; top: 498px; width: 485px; height: 1px; background: linear-gradient(90deg, transparent, var(--rule) 20%, var(--rule) 80%, transparent); }
  .contact { position: absolute; left: 0; width: 540px; text-align: center; font-size: 11.5px; color: var(--ink); line-height: 15px; }
  .contact--phone { top: 509px; }
  .contact--mail { top: 524px; }
  .contact em { font-style: italic; }

  .cover-art { position: absolute; inset: 0; }
  .cover-title {
    position: absolute; left: 40px; top: 20px; width: 345px; text-align: center;
    font-family: "Playfair Display", Georgia, serif; font-style: italic; font-weight: 700;
    color: var(--white); font-size: 27px; line-height: 39px; text-shadow: 1px 2px 3px rgba(0,0,0,.45);
  }
  .cover-title .small { font-size: 22px; }
</style>
</head>
<body>
  <main class="spread">
    <section class="page page--back">
      <div class="back-photo" role="img" aria-label="Oil pump jack silhouetted against an orange sunset sky"></div>

      <div class="about">
        <h2 class="about__title">Who We Are</h2>
        <h3 class="about__subtitle">Our Mission</h3>
        <p class="about__text">To provide professional solutions that allow our partners and clients to not only meet but exceed their objectives. Using a “Customer Vision” approach, we see your business and needs through your eyes to work together for the ultimate solution. Our goal is to help you achieve your goals. We emphasize achieving strong business results, faster time to market, getting the job done right, saving money, building an efficient organization and keeping your customers satisfied.</p>
      </div>

      <div class="brand brand--back"><span class="brand__dot"></span><span class="brand__name">Keldmoor Partners</span></div>

      <div class="contact-rule"></div>
      <p class="contact contact--phone">Contact Us <em>1-403-555-0142</em> | Fax.<em>1-403-555-0143</em></p>
      <p class="contact contact--mail">Email Us : <em>sales@keldmoorpartners.com</em> | 410, 2280 Harlow Street S.W., Calgary, Alberta, Canada T2R 1H6</p>
    </section>

    <section class="page page--cover">
      <svg class="cover-art" width="555" height="553" viewBox="0 0 555 553">
        <defs>
          <linearGradient id="field-photo" x1="0" y1="0" x2="0" y2="1">
            <stop offset="0" stop-color="#4f8fd0"/>
            <stop offset="0.45" stop-color="#9cbfe0"/>
            <stop offset="0.7" stop-color="#d8c24a"/>
            <stop offset="1" stop-color="#3a3a3a"/>
          </linearGradient>
        </defs>
        <polygon points="0,0 505,0 435,105 220,220" fill="var(--brand-blue)"/>
        <polygon points="505,0 555,0 555,195 435,105" fill="var(--brand-orange)"/>
        <polygon points="220,220 435,105 555,195 555,320 435,440" fill="url(#field-photo)" role="img" aria-label="Hand using a rugged field tablet in front of yellow oilfield pump jacks"/>
        <line x1="0" y1="0" x2="435" y2="440" stroke="#ffffff" stroke-width="3" opacity=".8"/>
        <line x1="4" y1="0" x2="439" y2="440" stroke="#8d8e90" stroke-width="1.5" opacity=".6"/>
      </svg>

      <h1 class="cover-title">Mergers &amp; Acquisition<br><span class="small">in the</span> oil &amp; gas<br>industry</h1>

      <div class="brand brand--cover"><span class="brand__dot"></span><span class="brand__name">Keldmoor Partners</span></div>
    </section>
  </main>
</body>
</html>
```